Lueur de Provins Immerse in the enchanting flavors of France at Lueur de Provins

A menu that is French in style with the Eiffel Tower. A elegant menu that is in rich blue with red or gold trimmings, we are a French Bakey and Cafe

Target Market(s)

30 to 55 people

Industry/Entity Type

Restaurant

Font styles to use
Decorative

Colors
0054AA
0677BA
7BADD7
CADEEF
E8F1F8
EB3D1F
EC4F4E
F09395
F8D3D4
FCEDEE

Requirements
Must have
• the attachment "My Brunch Specials" is the Menu I want you to create, it has all the text, "My Brunch Special Complete" is a word version. The menu size should be 4 1/4 wide by 14 inches long 2 Sided. must have our logo at the top , Make the font larger, because our biggest complaint about our menu is it is hard to read
Nice to have
• I would love to incorporate the Eiffel Tower as a silhouette in the background
Should not have
• I do not want too many pictures or small print

```html
<!DOCTYPE html>
<html lang="en">
<head>
<meta charset="utf-8">
<title>Lueur de Provins — Brunch &amp; Drink Specials</title>
<link href="https://fonts.googleapis.com/css2?family=Cinzel:wght@400;500&family=Roboto+Condensed:wght@300;400&family=Oswald:wght@400&display=swap" rel="stylesheet">
<style>
  :root{
    --navy:#1f2a4a;
    --red:#b23a36;
    --ink:#363636;
    --price:#a3a3a3;
    --rule:#9a9a9a;
    --paper:#fdfdfd;
    --stage:#ffffff;
    --tower-a:#eef0f3;
    --tower-b:#f8f9fa;
  }
  *{box-sizing:border-box;margin:0;padding:0}
  html,body{width:1200px;height:1200px;overflow:hidden;background:var(--stage)}
  .board{position:relative;width:1200px;height:1200px}
  .page-label{position:absolute;top:42px;width:120px;text-align:center;font-family:"Oswald",sans-serif;font-size:19px;color:#555;letter-spacing:.5px}
  .menu-page{position:absolute;top:89px;width:308px;height:1014px;background:var(--paper);box-shadow:0 1px 4px rgba(0,0,0,.35);overflow:hidden}
  .menu-page::after{content:"";position:absolute;left:0;right:0;bottom:0;height:6px;background:linear-gradient(var(--red) 0 2px,var(--navy) 2px 6px)}
  .tower-bg{position:absolute;left:0;top:140px;width:130px;height:860px;background:linear-gradient(90deg,var(--tower-a),var(--tower-b) 70%,transparent);clip-path:polygon(0 0,25% 0,40% 45%,100% 100%,0 100%)}
  .brand{position:absolute;left:0;right:0;text-align:center;font-family:"Roboto Condensed",sans-serif;font-size:7.5px;letter-spacing:3.4px;color:var(--navy);text-transform:uppercase}
  .brand-mark{display:block;width:20px;height:20px;margin:0 auto 8px;background:var(--navy)}
  .section-title{position:absolute;left:0;right:0;display:flex;align-items:center;justify-content:center;gap:6px;font-family:"Cinzel",serif;font-size:20px;letter-spacing:.5px}
  .section-title .rule{width:22px;height:1px;background:currentColor;position:relative}
  .section-title .rule::before{content:"";position:absolute;top:-2px;width:5px;height:5px;border-radius:50%;background:currentColor}
  .section-title .rule.l::before{left:0}
  .section-title .rule.r::before{right:0}
  .section-title .dot{font-size:9px}
  .title-red{color:var(--red)}
  .title-navy{color:var(--navy)}
  .title-navy .dot,.title-navy .rule{color:var(--red)}
  .menu-item{position:absolute;left:27px;right:14px}
  .item-head{display:flex;align-items:center;gap:5px;font-family:"Cinzel",serif;font-size:12.5px;color:#2b2b2b;line-height:14px}
  .item-head .name{white-space:nowrap}
  .item-head .line{flex:1;height:1px;background:var(--rule);margin-left:4px;max-width:90px}
  .item-head .spacer{flex:1}
  .item-head .star{font-size:9px;color:var(--navy)}
  .item-head .price{background:var(--price);color:#fff;font-size:11px;padding:1px 4px;min-width:26px;text-align:center}
  .item-head.accent .name{color:#3f5fa0}
  .item-desc{margin-top:4px;width:262px;font-family:"Roboto Condensed",sans-serif;font-weight:300;font-size:9.3px;line-height:11.7px;color:var(--ink)}
  .two-line .name{white-space:normal;line-height:13px}
</style>
</head>
<body>
<main class="board">
  <div class="page-label" style="left:320px">PAGE 1</div>
  <div class="page-label" style="left:730px">PAGE 2</div>

  <section class="menu-page" style="left:226px" aria-label="Brunch specials">
    <div class="tower-bg" role="img" aria-label="Faint Eiffel Tower silhouette in the background"></div>
    <div class="brand" style="top:18px"><span class="brand-mark"></span>Lueur de Provins</div>
    <h1 class="section-title title-red" style="top:90px"><span class="rule l"></span>BRUNCH<span class="dot">✦</span>SPECIALS<span class="rule r"></span></h1>

    <article class="menu-item" style="top:139px">
      <div class="item-head"><span class="name">Ratatouille &amp; Eggs</span><span class="line"></span><span class="spacer"></span><span class="star">✦</span><span class="price">$18</span><span class="star">✦</span></div>
      <p class="item-desc">Experience the essence of Provence with our Ratatouille, a vibrant medley of roasted squash, peppers, tomatoes, eggplant, infused with fragrant fresh herbs. Served with two perfectly poached eggs, and your choice of flavorful andouille sausage or crispy bacon. Accompanied by a side of crusty baguette. It's a hearty dish that celebrates the flavors of the Mediterranean countryside.</p>
    </article>

    <article class="menu-item" style="top:261px">
      <div class="item-head"><span class="name">Le Grande Breakfast</span><span class="line"></span><span class="spacer"></span><span class="star">✦</span><span class="price">$15</span><span class="star">✦</span></div>
      <p class="item-desc">Start your day in style with our Le Grande Breakfast, a feast fit for royalty. Customize your morning indulgence with two eggs cooked to your preference, paired with either savory bacon or succulent chicken sausage. Choose between a freshly baked baguette or a buttery croissant to accompany your meal. Complete your breakfast by selecting from an array of sides including crispy hash browns, savory roasted potatoes, or a refreshing fruit salad. Bon appetit!</p>
    </article>

    <article class="menu-item" style="top:406px">
      <div class="item-head"><span class="name">Smoked Salmon Tartine</span><span class="line"></span><span class="spacer"></span><span class="star">✦</span><span class="price">$14</span><span class="star">✦</span></div>
      <p class="item-desc" style="margin-top:12px">Delight in the luxurious flavors of our Smoked Salmon Tartine, a culinary, masterpiece that elevates breakfast to new heights. Indulge in truffled scrambled eggs nestled atop smoked salmon, adorned with tangy pickled red onions, briny caper berries, crisp cucumber, juicy tomato, and peppery arugula. All artfully arranged on multigrain bread generously spread with herb-infused cream cheese.</p>
    </article>

    <article class="menu-item" style="top:548px">
      <div class="item-head"><span class="name">Le Benedict Salmon</span><span class="line"></span><span class="spacer"></span><span class="star">✦</span><span class="price">$14</span><span class="star">✦</span></div>
      <p class="item-desc">Savor the classic elegance of Eggs Benedict, featuring two perfectly poached eggs nestled on toasted English muffins, with luscious smoked salmon and ripe tomato slices crowned with a velvety lemon-infused Hollandaise sauce. A timeless brunch delight crafted to perfection.</p>
    </article>

    <article class="menu-item" style="top:658px">
      <div class="item-head"><span class="name">Salmon Atlantique</span><span class="line"></span><span class="spacer"></span><span class="star">✦</span><span class="price">$14</span><span class="star">✦</span></div>
      <p class="item-desc">Enjoy a bed of crisp mixed greens adorned with delicate smoked salmon, sweet golden raisins, creamy goat cheese, and crunchy walnuts. All dressed in a tantalizing balsamic vinaigrette that ties the elements together perfectly.</p>
    </article>

    <article class="menu-item" style="top:762px">
      <div class="item-head"><span class="name">Beef Bourguignon</span><span class="line"></span><span class="spacer"></span><span class="star">✦</span><span class="price">$18</span><span class="star">✦</span></div>
      <p class="item-desc">Indulge in our rich and comforting flavors of savory, tender beef slowly braised in red wine, creating a luscious sauce that envelops pearl onions, carrots, and mushrooms in a symphony of flavors. Served alongside buttered egg noodles. It's a hearty and soul-warming meal that promises pure culinary bliss.</p>
    </article>

    <article class="menu-item" style="top:872px">
      <div class="item-head"><span class="name">Tourte au Poulet</span><span class="line"></span><span class="spacer"></span><span class="star">✦</span><span class="price">$15</span><span class="star">✦</span></div>
      <p class="item-desc">Discover the indulgent flavors of our Tourte au Poulet, a savory delight that marries tender marinated chicken with the richness of Swiss cheese and the sweetness of onions, all encased in layers of flaky pastry. Topped with a savory mushroom medley and decadent bechamel sauce. A true comfort classic to delight your senses.</p>
    </article>
  </section>

  <section class="menu-page" style="left:636px" aria-label="Drink specials">
    <div class="tower-bg" role="img" aria-label="Faint Eiffel Tower silhouette in the background" style="top:180px"></div>
    <div class="brand" style="top:14px"><span class="brand-mark" style="width:16px;height:16px;margin-bottom:6px"></span>Lueur de Provins</div>
    <h1 class="section-title title-navy" style="top:68px"><span class="rule l"></span>DRINK<span class="dot">✦</span>SPECIALS<span class="rule r"></span></h1>

    <article class="menu-item" style="top:106px;left:20px">
      <div class="item-head"><span class="name">Bottomless Mimosa</span><span class="line"></span><span class="spacer"></span><span class="star">✦</span><span class="price">$18</span><span class="star">✦</span></div>
      <p class="item-desc">Embark on an endless journey of delight with our Bottomless Mimosa, featuring Vallonne champagne, infusing each sip with a sparkling sensation. Tailor your experience with your preferred flavor profile - opt for the timeless twist of classic orange juice or tangy cranberry juice for a refreshing zing. Continuously poured to ensure your glass is always full.</p>
    </article>

    <article class="menu-item" style="top:213px;left:22px">
      <div class="item-head"><span class="name">Apple Cider-Mimosa</span><span class="line"></span><span class="spacer"></span><span class="star">✦</span><span class="price">$9</span><span class="star">✦</span></div>
      <p class="item-desc">A delightful twist on the classic mimosa. Crafted with champagne and crisp apple cider. To elevate the experience, we adorn the glass with a caramel rim dipped in brown sugar, adding a touch of indulgent sweetness to every sip.</p>
    </article>

    <article class="menu-item" style="top:293px;left:22px">
      <div class="item-head two-line"><span class="name">Blood Orange<br>or Pineapple Spritz</span><span class="line"></span><span class="spacer"></span><span class="star">✦</span><span class="price">$12</span><span class="star">✦</span></div>
      <p class="item-desc">Introducing our vibrant spritz cocktail, a tantalizing blend of Marlow &amp; Finch's premium Cirrane Vodka, sweet vermouth, and a touch of sweetness from a carefully muddled sugar cube. This effervescent libation reaches new heights with the addition of bubbly Perlière, your choice of either Blood Orange or Pineapple syrup injects a burst of fruity allure into every sip.</p>
    </article>

    <article class="menu-item" style="top:411px;left:25px">
      <div class="item-head"><span class="name">Peach Bellini</span><span class="line"></span><span class="spacer"></span><span class="star">✦</span><span class="price">$9</span><span class="star">✦</span></div>
      <p class="item-desc">Try our perfectly balanced Peach Bellini with each sip you capture the crispness of champagne with the irresistible sweetness of peach. It's a sublime fusion of sophistication and sweetness.</p>
    </article>

    <article class="menu-item" style="top:484px;left:26px">
      <div class="item-head"><span class="name">Espresso Martini</span><span class="line"></span><span class="spacer"></span><span class="star">✦</span><span class="price">$10</span><span class="star">✦</span></div>
      <p class="item-desc">Enjoy a bed of crisp mixed greens adorned with delicate smoked salmon, sweet golden raisins, creamy goat cheese, and crunchy walnuts. All dressed in a tantalizing balsamic vinaigrette that ties the elements together perfectly.</p>
    </article>

    <article class="menu-item" style="top:568px;left:27px">
      <div class="item-head"><span class="name">Kir Royale</span><span class="line"></span><span class="spacer"></span><span class="star">✦</span><span class="price">$10</span><span class="star">✦</span></div>
      <p class="item-desc">Our Kir Royale is a delightful fusion of the crisp, sparkling champagne bubbles and the sweet sophistication of black currant. a luxurious and indulgent drink that's perfect for any occasion</p>
    </article>

    <h2 class="section-title title-navy" style="top:646px"><span class="rule l"></span><span class="dot">✦</span>LATTE<span class="dot">✦</span><span class="rule r"></span></h2>

    <article class="menu-item" style="top:690px;left:27px">
      <div class="item-head accent"><span class="name">Truffle Latte</span><span class="line"></span><span class="spacer"></span><span class="star">✦</span><span class="price">$6</span><span class="star">✦</span></div>
      <p class="item-desc">We start with rich Bellacroix chocolate, known for its velvety smoothness and intense flavor. Then, we add a drizzle of salted caramel, adding a perfect balance of sweetness and a hint of savory richness. Finally, we combine this delightful blend with perfectly steamed milk to create a creamy and indulgent latte that will satisfy even the most discerning palate.</p>
    </article>

    <article class="menu-item" style="top:800px;left:28px">
      <div class="item-head"><span class="name">Napoleon Latte</span><span class="line"></span><span class="spacer"></span><span class="star">✦</span><span class="price">$6</span><span class="star">✦</span></div>
      <p class="item-desc" style="margin-top:12px">We start with our rich espresso, renowned for its bold and robust character. Then, we add a luscious combination of hazelnut and vanilla syrup, creating a symphony of sweetness and nutty richness. As the final touch, we crown this masterpiece with the velvety smoothness of perfectly steamed milk.</p>
    </article>

    <article class="menu-item" style="top:902px;left:28px">
      <div class="item-head"><span class="name">Chai Latte</span><span class="line"></span><span class="spacer"></span><span class="star">✦</span><span class="price">$6</span><span class="star">✦</span></div>
      <p class="item-desc">Our robust chai tea concentrate, infused with a symphony of cinnamon, cardamom, cloves, and ginger, sets the stage for a journey of aromatic delight. Paired with velvety steamed milk, each sip offers a harmonious blend of bold spices and creamy richness. Topped with a sprinkle of cinnamon, it's the perfect finishing touch to this comforting treat.</p>
    </article>
  </section>
</main>
</body>
</html>
```